Velvet Nook need a simple quirky modern straight to the point brochure of our group, our project and

I need a 5-10-page website that captures the ethos and the identity of Velvet Nook which is a brand-new project and concept providing first class professional locations and facilities to perform in carefully chosen categories working on several existing platforms in teams enjoying the flexibility in our approach.
This is a project that has been planned for 3 years.
The adult webcam industry is growing annually and rapidly and its split into two main sections. The first section is the Independent Models that are usually found to be working in more developed and fortunate countries such as the UK, Canada, USA and Western Europe. These independent models work on the same platforms as everyone else but are working from their homes alone in a designated room at a convenient time and on their own personal accounts. This section is growing rapidly now especially in the UK as women are learning that this is a very good way to make extra money in a safe and professional manner on established websites across the world and it’s this word of mouth progression that has caused the recent flood of potential models appearing on the sites. Although this section is growing rapidly the percentage of models who are what we class as successful considerably lower than that of the other side of the industry.

This side of the industry are the webcam studios. A studio is a place where a model can work in her own allocated room amongst other models who work in their own room where the IT equipment and professional lighting is provided. These models tend to be more serious about the role of a webcam model and treat it as a proper job putting the right number of hours in making more effort on how they present themselves and, in most cases, using several platforms when they broadcast at any one time. It’s a proven fact that in general the theme seems to show women working in professional studios are more successful than that of the independent models even though they usually give 50% of their earning to the studio as a rental payment. These places/premises are usually found in less developed countries where money and opportunities to earn it are far greater. These nations include Romania (the capital of webcam world with over 2000 active studios operating at any one time) Others to mention are Russia, Columbia, China, Philippines, Latvia, and other Eastern European Countries.
The models are not in our view treat with the flexibility they deserve, and we feel the conditions that are imposed are generally designed to suit the studio not the model.

In the UK there are several large established "groups" that have a lot of models signed to their group, but the models work independently from home. We know through our research these models get the same split (50%) as the studio models we also know a lot about but work alone with no real training or support. These groups are mainly based in the United Kingdom and USA and the numbers of the models joining them is growing at a ridiculous rate. The models also tend to be what we feel treat as another bum on a seat and the business plan seems to be the more models that sign the more the group account make.

Velvet Nook is completely different. We want to set up designated Studios that are accessible to all our models where we can professionally train support and advise new models and offer them the freedom and flexibility to work in our professional operated studios and their own homes which brings both sides of the industry together into one.

Velvet Nook is a group and idea that has formed from what can only be described as a spiritual special journey. Perfect foundations we feel to build something unique and magical.

We are a small team at the moment that come from different cultures, countries with diverse and valuable life experiences. Combined in unity our experiences skills and knowledge are better shared as we now work closely together preparing the start of this exciting new project. We have formed into what we believe is a very strong team over a very natural unplanned three-year period and together we share the same ethos, positive energies and vision as we move forward towards achieving our goals and our dream.

Our goal is to create very special groups of different types of people similar to ourselves who we believe will help us provide a very welcome refreshing change to how video chat is currently offered, performed, directed and received in the UK and beyond.

To achieve our goals, we believe we should start by creating special places where we can professionally introduce the industry, the right things to know and to do, the ins and the outs, answering all your questions properly whilst offering our honest opinions and advice.
We want these places to provide the unique rewards, the most creative, original and exciting incentives. Places where there is always quality home cooked food provided. Places that look after the responsibilities of buying expensive outfits and costumes or shoes or boots. Places that understand that make up and cosmetics are expensive and help buy the things that our models need.
We don’t want these places to imply strict rules and silly policies or even have people who think they are in charge but offer no benefit to themselves never mind the team. A place that shows you the easiest way to do this having the most fun and laughing the hardest.
Places that we know where everyone will make special and even much needed friends. We are now ready to set up our first studio premises which will offer the very best carefully and professionally thought out introductions for anybody who would like to see for themselves just how interesting, opportunistic, fun and rewarding the wonderful world of webcamming/video chat is and will continue to be for some time to come.
Believe us when we say anybody can do this, have fun and be successful.
The first webcam studio is based in Sheffield, South Yorkshire, England and is first instalment of what will become successful Venture Harbour franchise and original Adult brand that dares to break the rules to make a positive difference for everyone

The Studio is going to be called Velvet Nook and the slogan we have adopted which is important is "your secret sanctuary" which hits the nail on the head considering what we are opening our project from a location point of view. We will be using houses or residential properties initially and converting them into purpose build training studios with carefully thought out room designing with themes and classy vintage boutique styling. We will be focusing on more classy outfits for the models to wear which will be provided and all the areas of the studio will have quirky touches - (ideas - jukebox, stylising areas, home cooked cuisine available for the girls to eat, wine and other refreshments, chill out areas, potentially a child free zone. gym equipment and maybe a solarium to give you a better idea)
The focus and theme around the branding is teamwork, helping, caring, encouraging, incentivising and having fun making very good money in healthy environments - basically using my experience from being a sales director for a small then large IT company for 12 years (where I broke all the corporate rules to achieve the same ethos above)
Main message is probably flexibility, care and respect and the fact that this job is not exactly how a person who imagines it sees it exactly for what it is. We are thinking out of the box and putting all the good things ideas and experiences together and taking all the bad things, we have seen and experienced out of the mix. We all must create a place where the models would all agree and promote the slogans message - "your secret sanctuary"
perfect for single mums, students, people who need to earn more money that their main income, curious ladies or ladies who have lost their personal confidence for whatever reason (usually a man’s fault) also perfect for people who love working in teams.
I want the website to be a classy straight to the point brochure of our brand and ethos to create an image that can grow as we move forward. It MUST provide the following ...
1 - Flexibility to be changed easily by me or my team
2 - We have signed up to a corporate business portal on www.dombarrow-hub.co.uk which is a business portal, and, in that subscription, we have paid for a domain name (www.velvetnook-live.com) and we can host our site from their portal. I have no idea how to do this so will need help please.
3 - the ability to receive requests from models and distribute them to assigned mailboxes/email addresses.
4 - IMPORTANT
The ability and option to be upgraded to be able to offer live video streaming directly from our own group and website which eradicates the issue where we must pay between 30 -40% of the money we make to the websites we currently work on and where we are experienced. Examples of the sites we will use are Pinlark.com - glowmerry.com and quillbeam.com (mainly the first two)
I would love to be able to upgrade the website after we have settled into the project and be able to stream directly from our studios or independent model’s location. This would have to be very simple for the model to use and the customer and I would say glow Merry is the best example of how simple it needs to be. For this to be achieved we would need to have the facility to write profiles for each model, show their status (live etc) and be able to take payments from members to be used as purchase tokens to be redeemed within the site with our models. Something for the future and the ability to partner with a person or team to achieve this target would be ideal and a natural progression.

5 - the ability to play chosen music on certain pages with admin flexibility to change

6 - the ability to play videos that we may design for marketing purposes.

7 - Some sort of tracking device or system that can alert us of anyone who clicks on a certain location providing potential leads for us to follow. (least important)

I have tried to do this myself using the many build your own websites that are available, but I have given up. I want something as perfect as possible projecting our ethos and direction as clearly and quirky as possible.

Side Notes - there are lots of opportunities posted on job groups on Neighbrly that when we consider the feedback from people using them seem to be fake or offering people false and unrealistic opportunities. We want to focus on these groups in our marketing campaigns but somehow make the point that we are aware there are lots of let’s say amazing jobs out there on these Neighbrly groups that do not always meet people’s expectations in the end. Velvet Nook is real, and we do what we say.
I’m a very spiritual person and also an expert in astrology. I am also interested in numerology. I would like to in a very subtle quirky way include something in the deign related to spirituality, to my number in numerology which is number 11 and to my sign which is Sagittarius. I can help people using my knowledge and skills surrounding these interests and I have a proven track record when working as a director in corporate IT sales.

We have set up a limited business (Dorvel Limited) which will be the company owning any trading name such as Velvet Nook but for the first six months I want to class this a project before officially stating the business details online.

I have the logos designed that I will include. The picture that is a cross with Miro Benedek is a logo for a clothing designer i love so I sent. Also included are some screenshots from the attempts I made trying to design a website : )
Colours to consider - Grey shades - Pink - white - sage/olive green

Any questions please ask

Thanks
Tomas

students - single mums any openminded women wanting to work as part of a team via our studio premises or the flexibilty to work from home in sheffield and south yorkshire initially

• It MUST provide the following ...
• 1 - Flexibility to be changed easily by me or my team
• 2 - We have signed up to a corporate business portal on www.dombarrow-hub.co.uk which is a business portal, and, in that subscription, we have paid for a domain name (www.velvetnook-live.com) and we can host our site from their portal. I have no idea how to do this so will need help please.
• 3 - the ability to receive requests from models and distribute them to assigned mailboxes/email addresses.
• 4 - IMPORTANT
• The ability and option to be upgraded to be able to offer live video streaming directly from our own group and website which eradicates the issue where we must pay between 30 -40% of the money we make to the websites we currently work on and where we are experienced. Examples of the sites we will use are Pinlark.com - glowmerry.com and quillbeam.com (mainly the first two)
• I would love to be able to upgrade the website after we have settled into the project and be able to stream directly from our studios or independent model’s location. This would have to be very simple for the model to use and the customer and I would say glow Merry is the best example of how simple it needs to be. For this to be achieved we would need to have the facility to write profiles for each model, show their status (live etc) and be able to take payments from members to be used as purchase tokens to be redeemed within the site with our models. Something for the future and the ability to partner with a person or team to achieve this target would be ideal and a natural progression.
• 5 - the ability to play chosen music on certain pages with admin flexibility to change
• 6 - the ability to play videos that we may design for marketing purposes.
• 7 - Some sort of tracking device or system that can alert us of anyone who clicks on a certain location providing potential leads for us to follow. (least important)
• A simplke functioning online form where models can apply for opportunities or register their interest.
• All in the project description

```html
<!DOCTYPE html>
<html lang="en">
<head>
<meta charset="utf-8">
<title>Velvet Nook — Your Secret Sanctuary</title>
<link href="https://fonts.googleapis.com/css2?family=Open+Sans:wght@400;600;700&display=swap" rel="stylesheet">
<style>
:root{
  --pink:#c4085e;
  --pink-hot:#d0095f;
  --ink:#121212;
  --line:#2a2a2a;
  --white:#ffffff;
  --sage:#a9c08f;
  --live:#2ecc2e;
  --away:#ff1a1a;
}
*{box-sizing:border-box;margin:0;padding:0}
html,body{width:747px;height:1200px;overflow:hidden}
body{position:relative;background:var(--ink);font-family:"Open Sans",sans-serif;color:var(--white)}
.top-rule,.bottom-rule{position:absolute;left:0;width:747px;height:4px;background:var(--pink-hot)}
.top-rule{top:0}.bottom-rule{bottom:0}

.header{position:absolute;top:4px;left:0;width:747px;height:61px;border-bottom:1px solid var(--line)}
.brand{position:absolute;left:0;top:0;width:164px;height:61px;border-right:1px solid var(--line);display:flex;flex-direction:column;justify-content:center;align-items:center}
.brand-name{font-size:19px;font-weight:600;color:var(--pink-hot);line-height:1}
.brand-tag{font-size:5px;letter-spacing:1.6px;color:var(--pink-hot);margin-top:4px}
.search{position:absolute;left:258px;top:17px;width:232px;height:25px;border:1px solid #333;background:#151515;display:flex;align-items:center;justify-content:space-between;padding:0 14px 0 16px;font-size:8px;color:#ccc}
.btn-join{position:absolute;left:503px;top:16px;width:75px;height:26px;border-radius:13px;background:var(--sage);font-size:9px;font-weight:600;display:flex;align-items:center;justify-content:center}
.btn-login{position:absolute;left:585px;top:15px;width:69px;height:26px;border-radius:13px;border:1px solid var(--white);font-size:9px;font-weight:600;display:flex;align-items:center;justify-content:center}
.lang{position:absolute;left:668px;top:19px;width:62px;height:21px;border:1px solid #333;display:flex;align-items:center;justify-content:center;gap:5px;font-size:7px;font-weight:700}
.lang-flag{width:17px;height:10px;background:repeating-linear-gradient(#b22234 0 1.4px,#fff 1.4px 2.8px);position:relative}
.lang-flag::before{content:"";position:absolute;left:0;top:0;width:7px;height:5.6px;background:#3c3b6e}

.sidebar{position:absolute;left:0;top:65px;width:164px;height:1135px;background:radial-gradient(ellipse at 30% 40%,#1d1d1d,#101010 70%)}
.nav-item{height:39.6px;border-bottom:1px solid var(--line);display:flex;align-items:center;justify-content:space-between;padding:0 24px 0 25px;font-size:9px;font-weight:700}
.nav-item.active{background:var(--pink-hot);border-bottom-color:var(--pink-hot)}

.hero{position:absolute;left:164px;top:65px;width:583px;height:196px;background:radial-gradient(ellipse at 30% 50%,#5e0f33,#3a0a1f 75%)}
.hero-title{position:absolute;left:50px;top:56px;font-size:38px;font-weight:600;color:var(--white);line-height:1}
.hero-tag{position:absolute;left:66px;top:133px;font-size:9px;letter-spacing:3.3px}
.hero-art{position:absolute;left:290px;top:0;width:293px;height:196px;background:
  radial-gradient(ellipse 70px 110px at 82% 60%,#e2247f,rgba(226,36,127,0) 100%),
  radial-gradient(ellipse 150px 70px at 45% 55%,rgba(214,22,112,.75),rgba(214,22,112,0) 100%),
  linear-gradient(90deg,rgba(58,10,31,0),rgba(120,14,62,.5))}
.hero-play{position:absolute;left:551px;top:157px}

.gallery{position:absolute;left:164px;top:261px;width:583px;height:832px;background:var(--pink)}
.grid{position:absolute;left:16px;top:12px;display:grid;grid-template-columns:repeat(4,131px);column-gap:9px;row-gap:6.6px}
.card{height:179px;text-align:center}
.card-photo{position:relative;height:111px;overflow:hidden}
.card-photo::after{content:"";position:absolute;inset:0;background:radial-gradient(ellipse at 50% 45%,rgba(0,0,0,0) 45%,rgba(0,0,0,.35) 100%)}
.p1{background:radial-gradient(ellipse 30px 45px at 50% 50%,#c9a488,rgba(201,164,136,0)),radial-gradient(circle at 80% 20%,#7a6a3a,rgba(0,0,0,0) 50%),linear-gradient(160deg,#3b3a26,#1b1a12)}
.p2{background:radial-gradient(ellipse 35px 40px at 55% 45%,#f1d8c8,rgba(241,216,200,0)),radial-gradient(ellipse at 35% 80%,#a0284a,rgba(0,0,0,0) 55%),linear-gradient(160deg,#b89a8a,#5d3a34)}
.p3{background:radial-gradient(ellipse 55px 30px at 55% 55%,#e9cdb4,rgba(233,205,180,0)),radial-gradient(ellipse at 25% 55%,#3b4a4a,rgba(0,0,0,0) 45%),linear-gradient(160deg,#a49a84,#7c705c)}
.p4{background:radial-gradient(ellipse 35px 45px at 40% 55%,#b08068,rgba(176,128,104,0)),radial-gradient(circle at 85% 25%,#e0a050,rgba(0,0,0,0) 25%),linear-gradient(160deg,#4a3528,#1c130e)}
.p5{background:radial-gradient(ellipse 40px 40px at 40% 45%,#f2d0a8,rgba(242,208,168,0)),linear-gradient(160deg,#e8ddd0,#b59e82)}
.p6{background:radial-gradient(ellipse 45px 25px at 35% 50%,#9a7a6a,rgba(154,122,106,0)),radial-gradient(ellipse at 80% 80%,#111,rgba(0,0,0,0) 50%),linear-gradient(160deg,#6a6460,#2a2624)}
.p7{background:radial-gradient(ellipse 40px 40px at 45% 50%,#d8a888,rgba(216,168,136,0)),radial-gradient(ellipse at 30% 80%,#f0ece6,rgba(0,0,0,0) 50%),linear-gradient(160deg,#6a4a38,#2e2018)}
.p8{background:radial-gradient(ellipse 35px 25px at 55% 30%,#e0201a,rgba(224,32,26,0)),radial-gradient(ellipse 55px 35px at 45% 50%,#e8c4b0,rgba(232,196,176,0)),linear-gradient(160deg,#d8d4d0,#9a9490)}
.p9{background:radial-gradient(ellipse 35px 45px at 40% 50%,#c8a080,rgba(200,160,128,0)),radial-gradient(circle at 15% 20%,#c0a030,rgba(0,0,0,0) 40%),linear-gradient(160deg,#5a4a30,#2a2015)}
.p10{background:radial-gradient(ellipse 35px 25px at 45% 60%,#c01838,rgba(192,24,56,0)),radial-gradient(ellipse 50px 35px at 55% 55%,#c89070,rgba(200,144,112,0)),linear-gradient(180deg,#ece8e4 0 35%,#7a5a50)}
.p11{background:radial-gradient(ellipse 50px 35px at 50% 55%,#d0a488,rgba(208,164,136,0)),radial-gradient(ellipse at 70% 70%,#0e0e0e,rgba(0,0,0,0) 45%),linear-gradient(160deg,#4c4c50,#1c1c1e)}
.p12{background:radial-gradient(ellipse 30px 45px at 40% 45%,#ecd8c0,rgba(236,216,192,0)),radial-gradient(ellipse at 45% 85%,#e8e8e8,rgba(0,0,0,0) 45%),linear-gradient(90deg,#7a6a5a,#3a2a22)}
.p13{background:radial-gradient(ellipse 45px 40px at 50% 55%,#e0b89a,rgba(224,184,154,0)),radial-gradient(ellipse at 30% 25%,#3a2820,rgba(0,0,0,0) 40%),linear-gradient(160deg,#d8d4ce,#a8a29a)}
.p14{background:radial-gradient(ellipse 40px 45px at 50% 55%,#b88a70,rgba(184,138,112,0)),radial-gradient(ellipse at 70% 20%,#111,rgba(0,0,0,0) 45%),linear-gradient(160deg,#6a5048,#2e201c)}
.p15{background:radial-gradient(ellipse 30px 50px at 45% 50%,#e4c8b2,rgba(228,200,178,0)),linear-gradient(90deg,#4a4440,#2a2624 60%,#5a544e)}
.p16{background:radial-gradient(ellipse 28px 50px at 50% 55%,#f0ece6,rgba(240,236,230,0)),radial-gradient(circle at 12% 30%,#d8a838,rgba(0,0,0,0) 40%),linear-gradient(90deg,#8a6a30,#c8b080 60%,#e8c050)}
.card-bar{position:absolute;left:0;right:0;bottom:0;height:24px;display:flex;align-items:center;padding:0 10px;gap:5px;background:linear-gradient(transparent,rgba(0,0,0,.5));z-index:1}
.dot{width:8px;height:8px;border-radius:50%}
.dot.live{background:var(--live)}.dot.away{background:var(--away)}
.card-name{font-size:9.5px;font-weight:700;flex:1;text-align:left}
.card-text{margin-top:10px;font-size:8px;line-height:13px}
.card-btn{display:inline-block;margin-top:5px;width:64px;height:20px;border:1.5px solid var(--white);border-radius:10px;font-size:7.6px;font-weight:700;line-height:17px}
.show-more{position:absolute;left:225px;top:767px;width:134px;height:25px;border-radius:13px;background:var(--sage);font-size:8.5px;font-weight:600;display:flex;align-items:center;justify-content:center;letter-spacing:.3px}

.footer{position:absolute;left:164px;top:1093px;width:583px;height:103px}
.socials{position:absolute;top:20px;left:0;width:583px;display:flex;justify-content:center;gap:4px}
.social{width:22px;height:22px;border:1px solid var(--white);border-radius:50%;display:flex;align-items:center;justify-content:center}
.social::before{content:"";width:8px;height:8px;background:var(--white);border-radius:1px}
.footer-links{position:absolute;top:54px;width:583px;display:flex;justify-content:center;gap:9px;font-size:8px}
.copyright{position:absolute;top:77px;width:583px;text-align:center;font-size:6.5px}
</style>
</head>
<body>
<svg width="0" height="0" style="position:absolute">
  <symbol id="heart" viewBox="0 0 12 11"><path d="M6 10L1.3 5.3A2.7 2.7 0 0 1 6 1.8a2.7 2.7 0 0 1 4.7 3.5z" fill="none" stroke="#fff" stroke-width="1.2"/></symbol>
  <symbol id="chev" viewBox="0 0 7 5"><path d="M1 1l2.5 2.5L6 1" fill="none" stroke="#fff" stroke-width="1.2"/></symbol>
</svg>
<div class="top-rule"></div>

<header class="header">
  <div class="brand"><span class="brand-name">Velvet Nook</span><span class="brand-tag">YOUR SECRET SANCTUARY</span></div>
  <div class="search"><span>Search</span>
    <svg width="9" height="9" viewBox="0 0 10 10"><circle cx="4" cy="4" r="3" fill="none" stroke="#fff" stroke-width="1.5"/><line x1="6.3" y1="6.3" x2="9" y2="9" stroke="#fff" stroke-width="1.5"/></svg>
  </div>
  <div class="btn-join">JOIN NOW</div>
  <div class="btn-login">LOG IN</div>
  <div class="lang"><span class="lang-flag" role="img" aria-label="Flag"></span>ENG
    <svg width="6" height="4" viewBox="0 0 6 4"><path d="M0 0h6L3 4z" fill="#fff"/></svg>
  </div>
</header>

<nav class="sidebar">
  <div class="nav-item active">HOME</div>
  <div class="nav-item">ABOUT US</div>
  <div class="nav-item">SERVICE</div>
  <div class="nav-item">CONTACT</div>
  <div class="nav-item">CATEGORY <svg width="7" height="5"><use href="#chev"/></svg></div>
  <div class="nav-item">MORE <svg width="7" height="5"><use href="#chev"/></svg></div>
</nav>

<section class="hero">
  <div class="hero-art" role="img" aria-label="Pink illustration of a woman in profile with flowing ornamental hair"></div>
  <div class="hero-title">Velvet Nook</div>
  <div class="hero-tag">YOUR SECRET SANCTUARY</div>
  <svg class="hero-play" width="16" height="16" viewBox="0 0 16 16"><circle cx="8" cy="8" r="7.5" fill="#fff"/><path d="M6 4.5l5 3.5-5 3.5z" fill="#c4085e"/></svg>
</section>

<main class="gallery">
  <div class="grid">
    <div class="card"><div class="card-photo p1" role="img" aria-label="Model photo"><div class="card-bar"><span class="dot live"></span><span class="card-name">Occaecati</span><svg width="11" height="10"><use href="#heart"/></svg></div></div><p class="card-text">At vero eos et accusamus et iusto<br>odio dignissimos ducimus</p><span class="card-btn">SEE MORE</span></div>
    <div class="card"><div class="card-photo p2" role="img" aria-label="Model photo"><div class="card-bar"><span class="dot away"></span><span class="card-name">Occaecati</span><svg width="11" height="10"><use href="#heart"/></svg></div></div><p class="card-text">At vero eos et accusamus et iusto<br>odio dignissimos ducimus</p><span class="card-btn">SEE MORE</span></div>
    <div class="card"><div class="card-photo p3" role="img" aria-label="Model photo"><div class="card-bar"><span class="dot live"></span><span class="card-name">Occaecati</span><svg width="11" height="10"><use href="#heart"/></svg></div></div><p class="card-text">At vero eos et accusamus et iusto<br>odio dignissimos ducimus</p><span class="card-btn">SEE MORE</span></div>
    <div class="card"><div class="card-photo p4" role="img" aria-label="Model photo"><div class="card-bar"><span class="dot live"></span><span class="card-name">Occaecati</span><svg width="11" height="10"><use href="#heart"/></svg></div></div><p class="card-text">At vero eos et accusamus et iusto<br>odio dignissimos ducimus</p><span class="card-btn">SEE MORE</span></div>

    <div class="card"><div class="card-photo p5" role="img" aria-label="Model photo"><div class="card-bar"><span class="dot live"></span><span class="card-name">Occaecati</span><svg width="11" height="10"><use href="#heart"/></svg></div></div><p class="card-text">At vero eos et accusamus et iusto<br>odio dignissimos ducimus</p><span class="card-btn">SEE MORE</span></div>
    <div class="card"><div class="card-photo p6" role="img" aria-label="Model photo"><div class="card-bar"><span class="dot away"></span><span class="card-name">Occaecati</span><svg width="11" height="10"><use href="#heart"/></svg></div></div><p class="card-text">At vero eos et accusamus et iusto<br>odio dignissimos ducimus</p><span class="card-btn">SEE MORE</span></div>
    <div class="card"><div class="card-photo p7" role="img" aria-label="Model photo"><div class="card-bar"><span class="dot live"></span><span class="card-name">Occaecati</span><svg width="11" height="10"><use href="#heart"/></svg></div></div><p class="card-text">At vero eos et accusamus et iusto<br>odio dignissimos ducimus</p><span class="card-btn">SEE MORE</span></div>
    <div class="card"><div class="card-photo p8" role="img" aria-label="Model photo"><div class="card-bar"><span class="dot away"></span><span class="card-name">Occaecati</span><svg width="11" height="10"><use href="#heart"/></svg></div></div><p class="card-text">At vero eos et accusamus et iusto<br>odio dignissimos ducimus</p><span class="card-btn">SEE MORE</span></div>

    <div class="card"><div class="card-photo p9" role="img" aria-label="Model photo"><div class="card-bar"><span class="dot away"></span><span class="card-name">Occaecati</span><svg width="11" height="10"><use href="#heart"/></svg></div></div><p class="card-text">At vero eos et accusamus et iusto<br>odio dignissimos ducimus</p><span class="card-btn">SEE MORE</span></div>
    <div class="card"><div class="card-photo p10" role="img" aria-label="Model photo"><div class="card-bar"><span class="dot live"></span><span class="card-name">Occaecati</span><svg width="11" height="10"><use href="#heart"/></svg></div></div><p class="card-text">At vero eos et accusamus et iusto<br>odio dignissimos ducimus</p><span class="card-btn">SEE MORE</span></div>
    <div class="card"><div class="card-photo p11" role="img" aria-label="Model photo"><div class="card-bar"><span class="dot live"></span><span class="card-name">Occaecati</span><svg width="11" height="10"><use href="#heart"/></svg></div></div><p class="card-text">At vero eos et accusamus et iusto<br>odio dignissimos ducimus</p><span class="card-btn">SEE MORE</span></div>
    <div class="card"><div class="card-photo p12" role="img" aria-label="Model photo"><div class="card-bar"><span class="dot away"></span><span class="card-name">Occaecati</span><svg width="11" height="10"><use href="#heart"/></svg></div></div><p class="card-text">At vero eos et accusamus et iusto<br>odio dignissimos ducimus</p><span class="card-btn">SEE MORE</span></div>

    <div class="card"><div class="card-photo p13" role="img" aria-label="Model photo"><div class="card-bar"><span class="dot away"></span><span class="card-name">Occaecati</span><svg width="11" height="10"><use href="#heart"/></svg></div></div><p class="card-text">At vero eos et accusamus et iusto<br>odio dignissimos ducimus</p><span class="card-btn">SEE MORE</span></div>
    <div class="card"><div class="card-photo p14" role="img" aria-label="Model photo"><div class="card-bar"><span class="dot live"></span><span class="card-name">Occaecati</span><svg width="11" height="10"><use href="#heart"/></svg></div></div><p class="card-text">At vero eos et accusamus et iusto<br>odio dignissimos ducimus</p><span class="card-btn">SEE MORE</span></div>
    <div class="card"><div class="card-photo p15" role="img" aria-label="Model photo"><div class="card-bar"><span class="dot live"></span><span class="card-name">Occaecati</span><svg width="11" height="10"><use href="#heart"/></svg></div></div><p class="card-text">At vero eos et accusamus et iusto<br>odio dignissimos ducimus</p><span class="card-btn">SEE MORE</span></div>
    <div class="card"><div class="card-photo p16" role="img" aria-label="Model photo"><div class="card-bar"><span class="dot away"></span><span class="card-name">Occaecati</span><svg width="11" height="10"><use href="#heart"/></svg></div></div><p class="card-text">At vero eos et accusamus et iusto<br>odio dignissimos ducimus</p><span class="card-btn">SEE MORE</span></div>
  </div>
  <div class="show-more">SHOW MORE MODELS</div>
</main>

<footer class="footer">
  <div class="socials">
    <span class="social" aria-label="Social link"></span>
    <span class="social" aria-label="Social link"></span>
    <span class="social" aria-label="Social link"></span>
    <span class="social" aria-label="Social link"></span>
    <span class="social" aria-label="Social link"></span>
  </div>
  <div class="footer-links">
    <span>Home</span><span>/</span><span>About Us</span><span>/</span><span>Service</span><span>/</span><span>Contact</span><span>/</span><span>Careers</span><span>/</span><span>Privacy Policy</span><span>/</span><span>Log in</span>
  </div>
  <p class="copyright">Copyrights © 2018, Velvet Nook.All rights reserved. Terms | Privacy</p>
</footer>

<div class="bottom-rule"></div>
</body>
</html>
```